Corvale Spine & Joint Business Card

Need a business card using the logo provided. I want brand side of the card to be grey with the logo in the center of the card in white.

On the other side I leave to the designers

Target Market(s)

Personal Injury Attorneys

Industry/Entity Type

Medical

Contact Information for Business Card

Name, CEO. Cell Phone, (Eastvale, Address, Phone) (Westmere, Address, Phone) (Northbrook, Address, Phone)

Colors

Designer to choose only greyscale colors for use in the design.

Requirements
Must have
• Logo by itself on one side

```html
<!DOCTYPE html>
<html lang="en">
<head>
<meta charset="UTF-8">
<title>Corvale Spine &amp; Joint Business Card</title>
<link href="https://fonts.googleapis.com/css2?family=Montserrat:wght@600&family=Poppins:wght@400;500&display=swap" rel="stylesheet">
<style>
  :root {
    --backdrop: #2c2c31;
    --brand-grey: #9db8c0;
    --accent: #8fb0ba;
    --paper: #ffffff;
    --body-text: #9a9a9a;
    --watermark: #eef0f2;
    --white: #ffffff;
  }
  * { margin: 0; padding: 0; box-sizing: border-box; }
  html, body {
    width: 1200px; height: 801px; overflow: hidden;
    background: var(--backdrop);
  }
  .canvas {
    position: relative; width: 1200px; height: 801px;
    display: flex; align-items: center; justify-content: center; gap: 50px;
  }
  .card {
    position: relative; width: 520px; height: 297px; overflow: hidden;
    box-shadow: 0 14px 30px rgba(0,0,0,0.45);
  }

  /* Brand side */
  .card--front {
    background: var(--brand-grey);
    display: flex; align-items: center; justify-content: center;
  }
  .brand-name {
    font-family: "Montserrat", sans-serif; font-weight: 600;
    font-size: 34px; letter-spacing: 0; line-height: 1;
    color: var(--white); white-space: nowrap;
  }

  /* Contact side */
  .card--back { background: var(--paper); display: flex; }
  .holder {
    width: 190px; background: var(--brand-grey); color: var(--white);
    display: flex; flex-direction: column; justify-content: center;
    padding-left: 24px;
  }
  .holder__name {
    font-family: "Montserrat", sans-serif; font-weight: 600;
    font-size: 16px; letter-spacing: 1px; text-transform: uppercase;
    white-space: nowrap;
  }
  .holder__title { font-family: "Poppins", sans-serif; font-size: 12px; margin-top: 4px; letter-spacing: 1px; }
  .holder__phone {
    font-family: "Poppins", sans-serif; font-size: 11px; margin-top: 8px;
    display: flex; align-items: center; gap: 6px; white-space: nowrap;
  }
  .holder__phone svg { width: 10px; height: 10px; }

  .locations {
    position: relative; flex: 1; padding: 34px 0 0 24px;
    font-family: "Poppins", sans-serif;
  }
  .spine-motif {
    position: absolute; right: 0; top: 0; width: 110px; height: 100%;
    background: linear-gradient(90deg, rgba(238,240,242,0) 0%, var(--watermark) 45%, var(--watermark) 100%);
  }
  .location { position: relative; margin-bottom: 18px; }
  .location__city {
    display: inline-block; color: var(--accent); font-size: 12px; font-weight: 500;
    border-bottom: 1px solid var(--accent); padding-bottom: 1px; margin-bottom: 4px;
  }
  .location__line {
    color: var(--body-text); font-size: 9.5px; line-height: 1.45;
    display: flex; align-items: center; gap: 5px; white-space: nowrap;
  }
  .location__line svg { width: 8px; height: 8px; }
</style>
</head>
<body>
<main class="canvas">

  <section class="card card--front" aria-label="Brand side">
    <h1 class="brand-name">Corvale Spine &amp; Joint</h1>
  </section>

  <section class="card card--back" aria-label="Contact side">
    <div class="holder">
      <p class="holder__name">Owen R. Hale</p>
      <p class="holder__title">CEO</p>
      <p class="holder__phone">
        <svg viewBox="0 0 10 10" aria-hidden="true"><rect x="2" y="0.5" width="6" height="9" rx="1" fill="none" stroke="currentColor" stroke-width="1"/></svg>
        (+1) 555 014 220
      </p>
    </div>

    <div class="locations">
      <div class="spine-motif" role="img" aria-label="Faint vertebrae decoration along the right edge"></div>

      <div class="location">
        <span class="location__city">Eastvale</span>
        <p class="location__line">218 Harbor Ridge Rd, Bayfield, California, 93512</p>
        <p class="location__line">
          <svg viewBox="0 0 10 10" aria-hidden="true"><path d="M2 1 L4 1 L4.8 3.2 L3.6 4.2 Q4.6 6 6 6.6 L7 5.4 L9 6.2 L9 8.2 Q5 9 1.5 4.5 Q1 2.5 2 1 Z" fill="var(--accent)"/></svg>
          (+1) 555 014 220
        </p>
      </div>

      <div class="location">
        <span class="location__city">Northbrook</span>
        <p class="location__line">218 Harbor Ridge Rd, Bayfield, California, 93512</p>
        <p class="location__line">
          <svg viewBox="0 0 10 10" aria-hidden="true"><path d="M2 1 L4 1 L4.8 3.2 L3.6 4.2 Q4.6 6 6 6.6 L7 5.4 L9 6.2 L9 8.2 Q5 9 1.5 4.5 Q1 2.5 2 1 Z" fill="var(--accent)"/></svg>
          (+1) 555 014 220
        </p>
      </div>

      <div class="location">
        <span class="location__city">Westmere</span>
        <p class="location__line">218 Harbor Ridge Rd, Bayfield, California, 93512</p>
        <p class="location__line">
          <svg viewBox="0 0 10 10" aria-hidden="true"><path d="M2 1 L4 1 L4.8 3.2 L3.6 4.2 Q4.6 6 6 6.6 L7 5.4 L9 6.2 L9 8.2 Q5 9 1.5 4.5 Q1 2.5 2 1 Z" fill="var(--accent)"/></svg>
          (+1) 555 014 220
        </p>
      </div>
    </div>
  </section>

</main>
</body>
</html>
```